Business Card Design

Plumbing business.
Looking for a simple but professional looking design.
There are two variations of the logo; white background and black background. The logo with the white background is the primary business logo.
Industry/Entity Type
Business
Contact Information for Business Card
Marcus Fenley
Owner/Licensed Plumber
0412 396 081
info@marcusfenleyplumbing.com.au
www.marcusfenleyplumbing.com.au
Lic. 63941
Look and feel
Each slider illustrates characteristics of the customer's brand and the style your logo design should communicate.

```html
<!DOCTYPE html>
<html lang="en">
<head>
<meta charset="utf-8">
<title>Marcus Fenley Plumbing – Business Card</title>
<link href="https://fonts.googleapis.com/css2?family=Questrial&display=swap" rel="stylesheet">
<style>
  :root {
    --teal: #3fb0b9;
    --teal-deep: #2f9ea8;
    --white: #ffffff;
    --ink: #1e1e1e;
    --backdrop: #a3a3a6;
    --card-shadow: rgba(0, 0, 0, 0.18);
  }
  * { box-sizing: border-box; margin: 0; padding: 0; }
  html, body {
    width: 1200px; height: 900px; overflow: hidden;
    background: var(--backdrop);
    font-family: "Questrial", sans-serif;
  }
  .stage {
    width: 1200px; height: 900px;
    display: flex; align-items: center; justify-content: center; gap: 60px;
  }
  .card {
    position: relative;
    width: 525px; height: 300px;
    border-radius: 4px;
    overflow: hidden;
    box-shadow: 0 10px 24px var(--card-shadow);
  }
  /* Front */
  .card--front { background: var(--teal); color: var(--white); }
  .card__photo {
    position: absolute; inset: 0;
    background: radial-gradient(ellipse at 70% 60%, rgba(255,255,255,0.16), rgba(255,255,255,0) 60%),
                linear-gradient(160deg, var(--teal) 0%, var(--teal-deep) 100%);
  }
  .card__front-content {
    position: relative; height: 100%;
    display: flex; flex-direction: column; align-items: center; justify-content: center;
  }
  .brand { display: flex; align-items: center; gap: 14px; }
  .brand__mark { width: 22px; height: 22px; background: currentColor; }
  .brand__name {
    font-size: 30px; letter-spacing: 2px; text-transform: uppercase; line-height: 1.1;
  }
  .brand__trade {
    margin-top: 6px; font-size: 14px; letter-spacing: 11px; text-transform: uppercase;
    text-align: center;
  }
  .website {
    margin-top: 34px; font-size: 13px; letter-spacing: 1.5px; text-transform: uppercase;
  }
  /* Back */
  .card--back { background: var(--white); color: var(--ink); padding: 36px 40px; }
  .card--back .brand__mark { background: var(--teal); width: 18px; height: 18px; }
  .card--back .brand__name { font-size: 22px; color: var(--ink); }
  .card--back .brand__trade { font-size: 11px; letter-spacing: 8px; text-align: left; margin-left: 32px; }
  .contact { margin-top: 44px; font-variant: small-caps; }
  .contact__name { color: var(--teal); font-size: 21px; line-height: 1; }
  .contact__role { font-size: 14px; margin-bottom: 14px; }
  .contact__line { font-size: 14px; line-height: 1.35; }
  .contact__label { color: var(--teal); }
  .contact__licence { margin-top: 12px; font-size: 14px; }
</style>
</head>
<body>
<main class="stage">
  <section class="card card--front">
    <div class="card__photo" role="img" aria-label="Faded photograph of plumbing pipes and fittings in teal tones"></div>
    <div class="card__front-content">
      <div class="brand">
        <span class="brand__mark"></span>
        <span class="brand__name">Marcus Fenley</span>
      </div>
      <div class="brand__trade">Plumbing</div>
      <div class="website">www.marcusfenleyplumbing.com.au</div>
    </div>
  </section>

  <section class="card card--back">
    <div class="brand">
      <span class="brand__mark"></span>
      <span class="brand__name">Marcus Fenley</span>
    </div>
    <div class="brand__trade">Plumbing</div>
    <div class="contact">
      <p class="contact__name">Marcus Fenley</p>
      <p class="contact__role">Owner/Licensed Plumber</p>
      <p class="contact__line"><span class="contact__label">P:</span> 0412 396 081</p>
      <p class="contact__line"><span class="contact__label">E:</span> info@marcusfenleyplumbing.com.au</p>
      <p class="contact__licence">LIC. 63941</p>
    </div>
  </section>
</main>
</body>
</html>
```